Psychotherapy Website - Based in London

I am a newly trained psychotherapist and need a new website for www.rosalindfaber.co.uk.

I offer therapy for addiction, relationships, trauma and many other issues people face in their lives.

I want the website to be welcoming, gentle, feminine and for people to feel safe.

I do not like a page site that scrolls through sections, rather each page should be separate. Here some examples that i like. Sectional rather than scrolled.

https://www.hettiemarsh.com/
https://www.thequietwardrooms.com/

The imagery should be around pink using the flower in the logo / wording and around the site:

Here is a link to the flower for ideas:
https://www.pictofind.net/search?q=pink+gerbera&rlz=2D4KQTW_en-GBGB415GB415&source=lnms&tbm=isch&sa=X&ved=7cvQRtrk482h3PxZTuKLmeNBwXW_1AtXpVlKDbOQBmFLB&biw=1500&bih=889&dpr=2

RosalindFaber
Compassionate Psychotherapy

Is the logo and subheader for the website. Please use a typeface for the name that is appealing and professional.

Type face similar NOT EXLUSIVLY - JUST AN IDEA like this:
https://glowtonicstudio.com/

Basic business card i created as a rough idea below.

I have also added the website copy.

The headers are

Homepage
About Me
Therapy
Common Questions
Blog
Contact Me

Target Market(s)

Clients who are dealing with stress, trauma, pain, addiction

Industry/Entity Type

Therapy and Psychology

Coding

Coded - Design and coding required

Number of Pages Required

5+ page

Font styles to use
Serif
Sans Serif
Script

Colors
0054AA
0677BA
7BADD7
CADEEF
E8F1F8
0094D4
00A9DD
6FCCEA
C7EBF8
E9F6FB
E54698
E96AAD
F1A4CE
F9D9EA
FCEFF6

Requirements
Must have
• Pink Gerbera Flower integrated into design
Nice to have
• Images but not to stock imagery. Needs to look authentic and natural
Should not have
• Stock images of people. Images are important but needs to feel REAL

```html
<!DOCTYPE html>
<html lang="en">
<head>
<meta charset="utf-8">
<title>Rosalind Faber – Compassionate Psychotherapy</title>
<link href="https://fonts.googleapis.com/css2?family=Playfair+Display:wght@400;700&family=Open+Sans:wght@400;600;700&display=swap" rel="stylesheet">
<style>
  :root{
    --pink:#E54698;
    --pink-mid:#E96AAD;
    --pink-soft:#F1A4CE;
    --pink-pale:#F9D9EA;
    --pink-mist:#FCEFF6;
    --ink:#1c1a1d;
    --white:#ffffff;
  }
  *{box-sizing:border-box;margin:0;padding:0}
  html,body{width:904px;height:1200px;overflow:hidden}
  body{position:relative;font-family:"Open Sans",sans-serif;color:var(--ink);background:var(--white)}
  .serif{font-family:"Playfair Display",serif}

  .hero{position:absolute;left:0;top:0;width:904px;height:418px;
    background:linear-gradient(180deg,#241f24 0%,#6d4d55 20%,#b97a5a 42%,#7c5760 62%,#3d3135 100%)}
  .hero-scene{position:absolute;inset:0;
    background:radial-gradient(ellipse 55% 45% at 28% 48%,rgba(232,160,60,.75),transparent 70%),
               radial-gradient(ellipse 45% 60% at 78% 35%,rgba(236,150,160,.55),transparent 70%),
               radial-gradient(ellipse 40% 65% at 62% 80%,rgba(40,32,40,.7),transparent 75%)}

  .brand{position:absolute;display:flex;align-items:center;gap:6px}
  .brand-dot{width:46px;height:46px;border-radius:50%;background:var(--pink);flex:none}
  .brand-name{font-family:"Playfair Display",serif;font-size:21px;line-height:1;white-space:nowrap}
  .brand-rule{height:1px;background:var(--pink-soft);margin:6px 0 5px}
  .brand-sub{font-size:10px;letter-spacing:.3px}
  .brand--header{left:118px;top:24px;color:var(--white)}
  .brand--footer{left:348px;top:1008px;color:var(--ink)}
  .brand--footer .brand-rule{background:var(--pink-pale)}

  .nav{position:absolute;left:379px;top:33px;display:flex;align-items:center;gap:16px;font-size:11px;color:var(--white)}
  .btn{display:inline-block;border-radius:15px;font-size:11px;text-align:center;line-height:28px;height:28px}
  .btn--pill{background:var(--pink-pale);color:var(--pink);padding:0 15px}
  .btn--ghost{border:1px solid var(--white);color:var(--white);padding:0 15px;line-height:26px}
  .nav .btn{margin-left:-2px}

  .hero-copy{position:absolute;left:125px;top:130px;color:var(--white)}
  .hero-title{font-family:"Playfair Display",serif;font-weight:700;font-size:23px;line-height:28px;text-transform:uppercase}
  .hero-lead{font-size:17.5px;line-height:25px;font-weight:600;margin:11px 0 17px -1px}

  .divider{position:absolute;left:409px;top:462px;width:86px;height:20px}
  .divider span{position:absolute;left:0;right:0;bottom:0;height:1px;background:#b9a9b2}
  .divider i{position:absolute;left:33px;bottom:0;width:20px;height:10px;border-radius:10px 10px 0 0;background:var(--pink)}

  .about-title{position:absolute;left:0;width:904px;top:492px;text-align:center;font-family:"Playfair Display",serif;font-size:29px;letter-spacing:.3px}
  .about-intro{position:absolute;left:0;width:904px;top:543px;text-align:center;font-size:9.7px;line-height:17px;letter-spacing:.2px}

  .portrait{position:absolute;left:122px;top:594px;width:290px;height:323px;border-radius:12px;border:4px solid var(--pink-pale);background:var(--white);padding:0}
  .portrait-fill{width:100%;height:100%;border-radius:9px;
    background:linear-gradient(180deg,#f0dcc4 0%,#e9cdb3 55%,#ee6f98 78%,#e95f8d 100%)}

  .about-body{position:absolute;left:453px;top:589px;width:330px;font-size:9.7px;line-height:17.2px;letter-spacing:.15px}
  .about-body p{margin-bottom:1.6px}
  .about-cta{position:absolute;left:451px;top:885px}

  .footer{position:absolute;left:0;top:925px;width:904px;height:241px;
    background:linear-gradient(180deg,var(--white) 0%,var(--pink-mist) 30%,#f7d3e6 100%)}
  .contact{position:absolute;display:flex;gap:9px;align-items:flex-start;font-size:10.5px;line-height:15px}
  .contact-icon{width:42px;height:42px;border-radius:50%;background:var(--pink-mid);flex:none;display:flex;align-items:center;justify-content:center}
  .contact-label{font-weight:700;font-size:12px;line-height:16px}
  .contact--address{left:122px;top:1083px}
  .contact--phone{left:390px;top:1083px}
  .contact--email{left:604px;top:1083px}
  .contact--phone .contact-text,.contact--email .contact-text{padding-top:8px}

  .bar{position:absolute;left:0;top:1166px;width:904px;height:34px;background:var(--pink);color:var(--white);font-size:9.8px}
  .bar-text{position:absolute;left:122px;top:10px}
  .social{position:absolute;right:122px;top:7px;display:flex;gap:3px}
  .social span{width:19px;height:19px;border:1px solid var(--white);border-radius:50%}
</style>
</head>
<body>

<header class="hero">
  <div class="hero-scene" role="img" aria-label="Photograph of a person on a rocky mountain peak at a pink and orange sunrise"></div>

  <div class="brand brand--header">
    <span class="brand-dot"></span>
    <div>
      <div class="brand-name">Rosalind Faber</div>
      <div class="brand-rule"></div>
      <div class="brand-sub">Compassionate Psychotherapy</div>
    </div>
  </div>

  <nav class="nav">
    <span>Home</span><span>About Me</span><span>Therapy</span><span>Common Questions</span><span>Blog</span>
    <span class="btn btn--pill">Contact Me</span>
  </nav>

  <div class="hero-copy">
    <h1 class="hero-title">I offer a range of<br>psychotherapeutic<br>approaches</h1>
    <p class="hero-lead">Including Transactional Analysis<br>Psychotherapy &amp; Relational Therapy.</p>
    <span class="btn btn--ghost">Contact Me</span>
  </div>
</header>

<section class="about">
  <div class="divider"><i></i><span></span></div>
  <h2 class="about-title">ABOUT ROSALIND FABER</h2>
  <p class="about-intro">Taking The First Steps Towards Engaging In Therapy Can Be A Very Personal Journey.<br>Whilst, it can be challenging, I will ensure to make this journey as safe and as comfortable for you as possible.</p>

  <div class="portrait"><div class="portrait-fill" role="img" aria-label="Portrait photograph of the therapist in a pink blouse"></div></div>

  <div class="about-body">
    <p>Psychotherapy can help you see your current situation in new light, depth and clarity. It can change old and unhelpful perspectives &amp; feelings about yourself and your life, &amp; ultimately help you make positive changes.? It might be the most important journey you’ll ever make. I provide a and non-judgmental space where any issues can be explored in complete confidentiality.</p>
    <p>My practice is based in Richmond, where the room is homely, comfortable and welcoming. I believe a good environment contributes to great therapy.</p>
    <p>Alternately, I am also available to provide therapy online, if this environment is more accommodating for my clients.</p>
    <p>I am passionate about improving mental health and committed to offering therapy to all individuals regardless of their age, race, culture, disability, sexual orientation, or socio-economic background.</p>
  </div>
  <span class="btn btn--pill about-cta">Contact Me</span>
</section>

<footer>
  <div class="footer" role="img" aria-label="Faint pink-tinted photograph of a misty lake and mountains"></div>

  <div class="brand brand--footer">
    <span class="brand-dot"></span>
    <div>
      <div class="brand-name">Rosalind Faber</div>
      <div class="brand-rule"></div>
      <div class="brand-sub">Compassionate Psychotherapy</div>
    </div>
  </div>

  <div class="contact contact--address">
    <span class="contact-icon">
      <svg width="22" height="22" viewBox="0 0 24 24" fill="none" stroke="#fff" stroke-width="1.4"><path d="M12 21s-6-6-6-11a6 6 0 0 1 12 0c0 5-6 11-6 11z"/><circle cx="12" cy="10" r="2.2"/></svg>
    </span>
    <div class="contact-text"><div class="contact-label">Address</div>12 Willow Lane, Hartfield<br>Surrey, KT9 4ZX</div>
  </div>

  <div class="contact contact--phone">
    <span class="contact-icon">
      <svg width="22" height="22" viewBox="0 0 24 24" fill="none" stroke="#fff" stroke-width="1.4"><path d="M5 4h4l2 5-2.5 1.5a11 11 0 0 0 5 5L15 13l5 2v4a2 2 0 0 1-2 2A16 16 0 0 1 3 6a2 2 0 0 1 2-2z"/></svg>
    </span>
    <div class="contact-text"><div class="contact-label">Phone Number</div>020 7946 0381</div>
  </div>

  <div class="contact contact--email">
    <span class="contact-icon">
      <svg width="22" height="22" viewBox="0 0 24 24" fill="none" stroke="#fff" stroke-width="1.4"><rect x="3" y="9" width="18" height="12" rx="1"/><path d="M3 9l9 7 9-7M7 11V3h10v8"/></svg>
    </span>
    <div class="contact-text"><div class="contact-label">Email Address</div>rf@rosalindfaber.co.uk</div>
  </div>

  <div class="bar">
    <span class="bar-text">Copyright © 2021 Rosalind Faber. All Rights Reserved.</span>
    <div class="social"><span></span><span></span></div>
  </div>
</footer>

</body>
</html>
```